Modern Label for cleaning products for the brand Voralux

We need a label design for our line of cleaning products. The label should feature our logo and an image to identify the product's intended use. I've added our logo and an image for use. This only concerns the design of the label on the front of the bottle.

Label dimensions:
Label 1 (500ml bottle with spray): width 58mm x height 115mm
Label 2: (1L bottle): width 73mm x height 140mm
The design must be consistent for both bottles which you find in the pictures.

The bottles to be labeled are white. See the attachment for a photo of the bottles.

The photo must also appear on the label to identify the product's intended use.

Product information:
Brand: Voralux
Product: Sanitary Cleaner

This text must be placed on the label:
"Cleans, descales & freshens. followed with this text: "Ideal for quick and powerful cleaning. A ready-to-use product for everyday use."

- Mention the seperate USP's: Sanitary, Bathroom, Toilet, Wet areas

Appearance: This is a consumer product, but it must have a professional appearance. We would like to see a design that use the color blue from our logo.

Target Market(s)

Consumers who take care of their homes and want to maintain it the correct (professional) way

Font styles to use
Sans Serif

Colors
0054AA
0677BA
7BADD7
CADEEF
E8F1F8

Requirements
Must have
• USP's + use of image and logo + blend in 1 design
Nice to have
• Keep the color of the logo in the design
Should not have
• Comic sans

```html
<!DOCTYPE html>
<html lang="en">
<head>
<meta charset="utf-8">
<title>Voralux Sanitary Cleaner – Front Labels</title>
<link href="https://fonts.googleapis.com/css2?family=Bebas+Neue&family=Oswald:wght@300;400;500&display=swap" rel="stylesheet">
<style>
  :root {
    --blue-deep: #0054AA;
    --blue-mid: #0677BA;
    --blue-soft: #7BADD7;
    --blue-pale: #CADEEF;
    --blue-mist: #E8F1F8;
    --ink: #1b1f24;
    --ink-soft: #2c3a4a;
    --lemon-text: #F2A20C;
    --lemon: #F7D43A;
    --page: #ffffff;
  }
  * { box-sizing: border-box; margin: 0; padding: 0; }
  html, body {
    width: 1200px; height: 1200px; overflow: hidden;
    background: var(--page);
  }
  .canvas { position: relative; width: 1200px; height: 1200px; }

  .label {
    position: absolute;
    bottom: 140px;
    border-radius: calc(var(--u) * 0.6);
    background: linear-gradient(180deg, var(--blue-mist) 0%, #dbe8f5 55%, var(--blue-pale) 100%);
    font-family: 'Oswald', sans-serif;
    color: var(--ink);
    text-align: center;
  }
  .label--spray { --u: 12.7px; left: 158px; width: 356px; height: 670px; }
  .label--litre { --u: 16px; left: 594px; width: 448px; height: 860px; }

  .label > * { position: absolute; left: 0; right: 0; line-height: 1; }

  .brand-tab {
    left: 50%; right: auto;
    top: calc(var(--u) * -3.2);
    width: calc(var(--u) * 6.4); height: calc(var(--u) * 6.4);
    margin-left: calc(var(--u) * -3.2);
    border-radius: 50%; background: var(--blue-mist);
    display: flex; align-items: center; justify-content: center;
  }
  .brand-dot {
    width: calc(var(--u) * 4.2); height: calc(var(--u) * 4.2);
    border-radius: 50%; background: var(--blue-deep);
  }
  .brand-name {
    top: calc(var(--u) * 2.6);
    font-weight: 500; font-size: calc(var(--u) * 2.25);
    color: var(--ink); letter-spacing: 0.02em;
  }
  .product-title { top: calc(var(--u) * 9); }
  .product-title h1 {
    position: relative; display: inline-block;
    font-family: 'Bebas Neue', sans-serif; font-weight: 400;
    font-size: calc(var(--u) * 3.4); line-height: 1;
    color: var(--ink); letter-spacing: 0.01em;
  }
  .sparkle {
    position: absolute; right: -0.75em; top: -0.55em;
    width: 0.9em; height: 0.9em;
  }
  .claims {
    top: calc(var(--u) * 12.4);
    font-weight: 300; font-size: calc(var(--u) * 1.55);
    letter-spacing: 0.05em; color: var(--ink);
  }
  .fragrance {
    top: calc(var(--u) * 16.2);
    height: calc(var(--u) * 2.85);
    display: flex; align-items: center; justify-content: center;
    gap: calc(var(--u) * 0.4);
    color: var(--lemon-text); font-weight: 400; font-size: calc(var(--u) * 1.15);
  }
  .fragrance__lemon {
    width: calc(var(--u) * 2.85); height: calc(var(--u) * 2.85); border-radius: 50%;
    background: radial-gradient(circle, #fff3a8 0%, var(--lemon) 55%, #f0c21e 100%);
    border: calc(var(--u) * 0.15) solid #fbe98a;
  }
  .description {
    top: calc(var(--u) * 21.1);
    font-weight: 300; font-size: calc(var(--u) * 1.12);
    line-height: calc(var(--u) * 1.5); color: var(--ink-soft);
  }
  .areas {
    top: calc(var(--u) * 25);
    display: flex; justify-content: center; gap: calc(var(--u) * 0.3);
    list-style: none;
  }
  .area { width: calc(var(--u) * 3.6); display: flex; flex-direction: column; align-items: center; }
  .area__tile {
    width: calc(var(--u) * 3.6); height: calc(var(--u) * 2.85);
    border-radius: calc(var(--u) * 0.4);
    background: var(--blue-pale);
    display: flex; align-items: center; justify-content: center;
  }
  .area__tile svg { width: calc(var(--u) * 2); height: calc(var(--u) * 2); }
  .area__name {
    margin-top: calc(var(--u) * 0.45);
    font-size: calc(var(--u) * 0.62); font-weight: 300; line-height: 1;
    color: var(--ink-soft);
  }
  .volume {
    top: calc(var(--u) * 30.55);
    font-weight: 300; font-size: calc(var(--u) * 1.2); color: var(--ink-soft);
  }
  .splash {
    top: calc(var(--u) * 32.6); bottom: 0;
    border-radius: 0 0 calc(var(--u) * 0.6) calc(var(--u) * 0.6);
    background:
      linear-gradient(172deg, transparent 0%, transparent 22%, rgba(6,119,186,0.5) 32%, rgba(0,84,170,0.7) 40%, rgba(123,173,215,0.55) 52%, rgba(202,222,239,0.5) 74%, rgba(123,173,215,0.75) 100%),
      linear-gradient(180deg, rgba(232,241,248,0) 0%, var(--blue-pale) 100%);
  }
</style>
</head>
<body>
<main class="canvas">

  <section class="label label--spray" aria-label="Front label, 500 ml spray bottle">
    <div class="brand-tab"><div class="brand-dot"></div></div>
    <p class="brand-name">voralux</p>
    <div class="product-title">
      <h1>Sanitary Cleaner
        <svg class="sparkle" viewBox="0 0 40 40" aria-hidden="true">
          <path d="M16 6 L19 19 L32 22 L19 25 L16 38 L13 25 L0 22 L13 19 Z" fill="var(--blue-mid)"/>
          <path d="M31 0 L32.4 5.6 L38 7 L32.4 8.4 L31 14 L29.6 8.4 L24 7 L29.6 5.6 Z" fill="var(--blue-mid)"/>
        </svg>
      </h1>
    </div>
    <p class="claims">CLEANS · DESCALES · FRESHENS</p>
    <div class="fragrance">
      <span>FRESH LEMON</span>
      <div class="fragrance__lemon" role="img" aria-label="Lemon slice"></div>
      <span>FRAGRANCE</span>
    </div>
    <p class="description">Ideal for quick and powerful cleaning.<br>A ready-to-use product for everyday use.</p>
    <ul class="areas">
      <li class="area"><div class="area__tile"><svg viewBox="0 0 24 24"><rect x="3" y="13" width="18" height="5" rx="2" fill="var(--blue-deep)"/><rect x="14" y="4" width="7" height="5" fill="none" stroke="var(--blue-deep)" stroke-width="1.5"/><rect x="16.5" y="9" width="2" height="10" fill="var(--blue-deep)"/></svg></div><span class="area__name">BATHROOM</span></li>
      <li class="area"><div class="area__tile"><svg viewBox="0 0 24 24"><path d="M5 20 V6 Q5 3 8 3 H10" fill="none" stroke="var(--blue-deep)" stroke-width="2"/><path d="M8 8 L14 6 L16 11 Z" fill="var(--blue-deep)"/><g fill="var(--blue-soft)"><circle cx="16" cy="14" r="1"/><circle cx="19" cy="13" r="1"/><circle cx="14" cy="17" r="1"/><circle cx="18" cy="17" r="1"/><circle cx="20" cy="16" r="1"/></g></svg></div><span class="area__name">SHOWER</span></li>
      <li class="area"><div class="area__tile"><svg viewBox="0 0 24 24"><rect x="13" y="3" width="6" height="9" rx="1" fill="var(--blue-deep)"/><path d="M4 11 H19 Q19 17 13 17 L14 21 H8 L9 17 Q4 16 4 11 Z" fill="var(--blue-deep)"/></svg></div><span class="area__name">TOILET</span></li>
      <li class="area"><div class="area__tile"><svg viewBox="0 0 24 24"><rect x="3" y="4" width="8" height="5" fill="var(--blue-deep)"/><path d="M14 9 L17 4 L20 9 Z" fill="var(--blue-deep)"/><rect x="3" y="11" width="8" height="9" fill="var(--blue-deep)"/><rect x="13" y="11" width="8" height="9" fill="none" stroke="var(--blue-deep)" stroke-width="1.6"/></svg></div><span class="area__name">KITCHEN</span></li>
    </ul>
    <p class="volume">500Ml (17 Oz.)</p>
    <div class="splash" role="img" aria-label="Photo of a clear blue water splash with bubbles"></div>
  </section>

  <section class="label label--litre" aria-label="Front label, 1 litre bottle">
    <div class="brand-tab"><div class="brand-dot"></div></div>
    <p class="brand-name">voralux</p>
    <div class="product-title">
      <h1>Sanitary Cleaner
        <svg class="sparkle" viewBox="0 0 40 40" aria-hidden="true">
          <path d="M16 6 L19 19 L32 22 L19 25 L16 38 L13 25 L0 22 L13 19 Z" fill="var(--blue-mid)"/>
          <path d="M31 0 L32.4 5.6 L38 7 L32.4 8.4 L31 14 L29.6 8.4 L24 7 L29.6 5.6 Z" fill="var(--blue-mid)"/>
        </svg>
      </h1>
    </div>
    <p class="claims">CLEANS · DESCALES · FRESHENS</p>
    <div class="fragrance">
      <span>FRESH LEMON</span>
      <div class="fragrance__lemon" role="img" aria-label="Lemon slice"></div>
      <span>FRAGRANCE</span>
    </div>
    <p class="description">Ideal for quick and powerful cleaning.<br>A ready-to-use product for everyday use.</p>
    <ul class="areas">
      <li class="area"><div class="area__tile"><svg viewBox="0 0 24 24"><rect x="3" y="13" width="18" height="5" rx="2" fill="var(--blue-deep)"/><rect x="14" y="4" width="7" height="5" fill="none" stroke="var(--blue-deep)" stroke-width="1.5"/><rect x="16.5" y="9" width="2" height="10" fill="var(--blue-deep)"/></svg></div><span class="area__name">BATHROOM</span></li>
      <li class="area"><div class="area__tile"><svg viewBox="0 0 24 24"><path d="M5 20 V6 Q5 3 8 3 H10" fill="none" stroke="var(--blue-deep)" stroke-width="2"/><path d="M8 8 L14 6 L16 11 Z" fill="var(--blue-deep)"/><g fill="var(--blue-soft)"><circle cx="16" cy="14" r="1"/><circle cx="19" cy="13" r="1"/><circle cx="14" cy="17" r="1"/><circle cx="18" cy="17" r="1"/><circle cx="20" cy="16" r="1"/></g></svg></div><span class="area__name">SHOWER</span></li>
      <li class="area"><div class="area__tile"><svg viewBox="0 0 24 24"><rect x="13" y="3" width="6" height="9" rx="1" fill="var(--blue-deep)"/><path d="M4 11 H19 Q19 17 13 17 L14 21 H8 L9 17 Q4 16 4 11 Z" fill="var(--blue-deep)"/></svg></div><span class="area__name">TOILET</span></li>
      <li class="area"><div class="area__tile"><svg viewBox="0 0 24 24"><rect x="3" y="4" width="8" height="5" fill="var(--blue-deep)"/><path d="M14 9 L17 4 L20 9 Z" fill="var(--blue-deep)"/><rect x="3" y="11" width="8" height="9" fill="var(--blue-deep)"/><rect x="13" y="11" width="8" height="9" fill="none" stroke="var(--blue-deep)" stroke-width="1.6"/></svg></div><span class="area__name">KITCHEN</span></li>
    </ul>
    <p class="volume">1 Litre (34 Oz.)</p>
    <div class="splash" role="img" aria-label="Photo of a clear blue water splash with bubbles"></div>
  </section>

</main>
</body>
</html>
```